Poster Needed for Church Conference

I need a poster for a weekend conference at my church. Looking to attract as many people as possible. We are a church in the suburbs of Houston. This is mainly for our own church members but we are opening it up to outside church members.

Please see previous design from last conference and all other graphic work that can (doesn't need to be) included.

Target Market(s)

It's targeted for all people. But our main audience is families. around the age of 30 should be main target.

Industry/Entity Type

Non-Profit

Font styles to use
Serif
Sans Serif

Colors

Designer to choose colors to be used in the design.

Requirements
Must have
• 11x17 design with ability to shrink and blow up. but ideally for 11x17
• Content and wording:
• "Rooted Light Conference: Bridging the gap between generations and passing on our deepest beliefs and values."
• Featuring Dr. Gil Marsden. Author of "The Path of P4"
• Aug 25-26: Friday 8-10 pm, Saturday 4-8 pm
• Cost Adults $15/Children $5: Covers admission to all sessions and workshops, refreshments and Saturday dinner. *kids 5 and under free
• Childcare provided for all sessions. "
• Please use church logo and address on flyer: 4312 Route 19, Missouri City, TX 77988
Nice to have
• Ideally it will be designed so that we can crop a 16:9 pp announcement slide and header for our website.
Should not have
• anything offensive

```html
<!DOCTYPE html>
<html lang="en">
<head>
<meta charset="utf-8">
<title>Rooted Light Conference</title>
<link href="https://fonts.googleapis.com/css2?family=Bebas+Neue&family=Oswald:wght@500&family=Architects+Daughter&family=Reenie+Beanie&family=Patrick+Hand&display=swap" rel="stylesheet">
<style>
  :root {
    --yellow: #f3e12a;
    --green: #a6d63a;
    --tape: rgba(238, 226, 170, 0.9);
    --tape-edge: rgba(214, 200, 140, 0.9);
    --ink: #1c1b17;
    --brand: #3fa35a;
    --white: #fdfdfb;
  }
  html, body { margin: 0; padding: 0; overflow: hidden; }
  .poster {
    position: relative;
    width: 1200px;
    height: 777px;
    overflow: hidden;
    background: var(--green);
    color: var(--ink);
  }
  .backdrop { position: absolute; inset: 0; }
  .tape {
    position: absolute;
    background: var(--tape);
    box-shadow: 0 2px 6px rgba(0,0,0,.12);
  }
  .tape-featuring { left: 124px; top: 0; width: 190px; height: 116px; }
  .featuring-label {
    position: absolute; left: 140px; top: 64px; margin: 0;
    font: 500 31px "Oswald", sans-serif; letter-spacing: .5px;
  }
  .polaroid {
    position: absolute; left: 100px; top: 118px; width: 290px; height: 318px;
    background: var(--white); transform: rotate(10deg);
    box-shadow: 0 4px 12px rgba(0,0,0,.25);
  }
  .speaker-photo {
    position: absolute; left: 16px; top: 16px; width: 258px; height: 212px;
    background: radial-gradient(circle at 55% 45%, #8a6f5e 0%, #3b2e28 35%, #0d0d0d 70%);
  }
  .speaker-caption {
    position: absolute; left: 22px; top: 232px; margin: 0;
    font: 25px/0.95 "Reenie Beanie", cursive;
  }
  .speaker-caption .name { font-size: 29px; letter-spacing: 1px; }
  .book-cover {
    position: absolute; left: 155px; top: 445px; width: 195px; height: 270px;
    transform: rotate(-4deg);
    background: linear-gradient(180deg, #f4f4f2 0%, #e4e6e2 55%, #47b05a 58%, #47b05a 64%, #f1f1ee 66%);
    box-shadow: 4px 6px 12px rgba(0,0,0,.3);
  }
  .tape-title {
    left: 440px; top: 95px; width: 700px; height: 255px;
    transform: rotate(-12deg);
    background: linear-gradient(180deg, var(--tape) 0%, var(--tape) 45%, rgba(214,235,180,.9) 60%, var(--tape) 100%);
  }
  .title-block {
    position: absolute; left: 490px; top: 100px; width: 620px;
    transform: rotate(-12deg); text-align: center;
  }
  .title {
    margin: 0; font: 92px/0.86 "Bebas Neue", sans-serif; letter-spacing: 2px;
  }
  .tagline {
    margin: 8px 0 0; font: 25px/1.05 "Patrick Hand", sans-serif;
  }
  .tape-info { left: 488px; top: 384px; width: 680px; height: 222px; transform: rotate(-1deg); }
  .info { position: absolute; left: 570px; top: 400px; width: 540px; }
  .dates { margin: 0; font: 42px "Bebas Neue", sans-serif; letter-spacing: 1px; white-space: nowrap; }
  .dates small { font-size: 26px; }
  .cost { margin: 0; font: 26px/1.2 "Architects Daughter", cursive; text-align: center; }
  .cost .label { font: 38px "Bebas Neue", sans-serif; float: left; margin-right: 4px; line-height: 1; }
  .childcare { margin: 4px 0 0 110px; font: 15px "Architects Daughter", cursive; }
  .tape-church { left: 592px; top: 634px; width: 482px; height: 136px; transform: rotate(-.5deg); }
  .church-name {
    position: absolute; left: 640px; top: 658px; margin: 0;
    display: flex; align-items: center; gap: 10px;
    font: 36px "Bebas Neue", sans-serif; color: var(--brand); letter-spacing: 1px;
  }
  .church-name .dot { width: 22px; height: 22px; border-radius: 50%; background: var(--brand); }
  .address {
    position: absolute; left: 592px; top: 728px; width: 482px; margin: 0;
    text-align: center; font: 17px "Patrick Hand", sans-serif;
  }
</style>
</head>
<body>
<main class="poster">
  <svg class="backdrop" width="1200" height="777" viewBox="0 0 1200 777" aria-hidden="true">
    <polygon points="0,0 1200,0 1200,112 0,364" fill="var(--yellow)"/>
  </svg>

  <div class="tape tape-featuring"></div>
  <p class="featuring-label">Featuring:</p>

  <figure class="polaroid" style="margin:0">
    <div class="speaker-photo" role="img" aria-label="Portrait photograph of the featured speaker"></div>
    <figcaption class="speaker-caption">
      <span class="name">Dr. Gil Marsden</span><br>
      Author of<br>
      "The Path of P4"
    </figcaption>
  </figure>

  <div class="book-cover" role="img" aria-label="Cover of the book The Path of P4 by Gil Marsden"></div>

  <div class="tape tape-title"></div>
  <header class="title-block">
    <h1 class="title">Rooted Light<br>Conference:</h1>
    <p class="tagline">"Bridging the gap between generations<br>and passing on our deepest beliefs and values."</p>
  </header>

  <div class="tape tape-info"></div>
  <section class="info">
    <p class="dates">Aug 25–26: &nbsp;Fri 8–10<small>PM</small>, &nbsp;Sat 4–8<small>PM</small></p>
    <p class="cost"><span class="label">Cost:</span> ADULTS $15 / CHILDREN $5:<br>
      Covers admission to all sessions and workshops, refreshments and Saturday dinner. *Kids 5 and under free*</p>
    <p class="childcare">Childcare provided for all sessions.</p>
  </section>

  <div class="tape tape-church"></div>
  <p class="church-name"><span class="dot"></span>Cedar Grove Community Church</p>
  <p class="address">4312 Route 19, Missouri City, TX 77988</p>
</main>
</body>
</html>
```